ORB Stationary and Biz cards
Please include the logo I have attached.
Simple
Dorotea Wellmont
dpalvane@qzr.example
www.orbworthkeeping.example
Hello,
I will provide the proper address in a few days. It will take one line for address and one for city and state.
I uploaded the entire file of my logo, not only the AI format. Please let me know if this is a problem. Thank you!
Please let me know if you cannot access the subfiles within this file for your use. Thanks!
Please let me know if you have problems opening the AI file in this attachment. Thank you!
ORB

```html
<!DOCTYPE html>
<html lang="en">
<head>
<meta charset="utf-8">
<title>ORB Stationery and Business Cards</title>
<link rel="stylesheet" href="https://fonts.googleapis.com/css2?family=Open+Sans:wght@400;600;700&display=swap">
<style>
  :root{
    --board:#e3cfa8;
    --paper:#ffffff;
    --blue:#1f6fc1;
    --blue-deep:#15549a;
    --green:#6dbb2f;
    --ink:#4a4a4a;
    --label:#6b5a3e;
    --ghost:#e6eef6;
    --shadow:rgba(60,40,10,.25);
  }
  *{box-sizing:border-box;margin:0;padding:0}
  html,body{width:1200px;height:446px;overflow:hidden}
  body{background:var(--board);font-family:"Open Sans",Arial,sans-serif;position:relative;color:var(--ink)}
  .sheet{position:absolute;background:var(--paper);box-shadow:0 2px 6px var(--shadow);overflow:hidden}
  .sheet svg.waves{position:absolute;inset:0;width:100%;height:100%}
  .label{position:absolute;font-size:6px;letter-spacing:.12em;text-transform:uppercase;color:var(--label)}
  .brand{position:absolute;display:flex;align-items:center;gap:4px}
  .brand-mark{width:6px;height:6px;background:var(--green)}
  .brand-name{font-weight:700;color:var(--blue)}
  .brand-tag{font-size:3px;line-height:1.25;color:var(--ink);text-transform:uppercase}
  .contact{position:absolute;font-size:3.6px;line-height:1.6;color:var(--ink)}
  .ghost-name{position:absolute;font-weight:700;color:var(--ghost);letter-spacing:.02em}

  .letterhead{top:17px;width:290px;height:408px}
  .letterhead-1{left:149px}
  .letterhead-2{left:473px}
  .letterhead .brand{left:112px;top:14px}
  .letterhead .brand-name{font-size:20px}
  .letterhead .contact{right:28px;top:14px}
  .letterhead .ghost-name{left:82px;top:150px;font-size:64px}

  .card{left:10px;top:211px;width:50px;height:34px}
  .card .brand{left:4px;top:8px;gap:2px}
  .card .brand-name{font-size:7px}
  .card .brand-mark{width:3px;height:3px}

  .envelope-back{left:864px;top:10px;width:330px;height:216px}
  .envelope-plain{left:864px;top:236px;width:330px;height:118px}
  .envelope-front{left:798px;top:293px;width:283px;height:112px}
  .envelope-front .brand{left:12px;top:10px}
  .envelope-front .brand-name{font-size:16px}
  .envelope-front .return{position:absolute;left:12px;top:36px;font-size:3.6px;color:var(--ink)}
</style>
</head>
<body>

<p class="label" style="left:10px;top:196px">Business Card Design</p>
<div class="sheet card">
  <svg class="waves" viewBox="0 0 50 34" preserveAspectRatio="none" aria-hidden="true">
    <path d="M0 26 C15 22 30 30 50 21 L50 34 L0 34Z" fill="var(--blue)"/>
    <path d="M0 25 C15 21 30 29 50 20 L50 21 C30 30 15 22 0 26Z" fill="var(--green)"/>
  </svg>
  <div class="brand"><span class="brand-mark"></span><span class="brand-name">ORB</span></div>
</div>

<div class="sheet letterhead letterhead-1">
  <svg class="waves" viewBox="0 0 290 408" preserveAspectRatio="none" aria-hidden="true">
    <path d="M0 0 L60 0 C30 6 10 18 0 34Z" fill="var(--blue)"/>
    <path d="M0 34 C10 18 30 6 60 0 L70 0 C38 8 14 22 0 40Z" fill="var(--green)"/>
    <path d="M0 372 C80 350 170 395 290 362 L290 408 L0 408Z" fill="var(--blue)"/>
    <path d="M0 366 C80 344 170 389 290 356 L290 362 C170 395 80 350 0 372Z" fill="var(--green)"/>
  </svg>
  <div class="brand"><span class="brand-mark"></span><span class="brand-name">ORB</span><span class="brand-tag">Outreach Regional<br>Bureau of Climate<br>Partners</span></div>
  <div class="contact">T 555 014 2200<br>F 555 014 2201<br>12 Ridge Lane<br>Aspen Falls CO<br>dpalvane@qzr.example</div>
  <div class="ghost-name">ORB</div>
</div>
<p class="label" style="left:250px;top:432px">Letterhead Option 1</p>

<div class="sheet letterhead letterhead-2">
  <svg class="waves" viewBox="0 0 290 408" preserveAspectRatio="none" aria-hidden="true">
    <path d="M0 0 L60 0 C30 6 10 18 0 34Z" fill="var(--blue)"/>
    <path d="M0 34 C10 18 30 6 60 0 L70 0 C38 8 14 22 0 40Z" fill="var(--green)"/>
    <path d="M0 360 C90 395 190 340 290 372 L290 408 L0 408Z" fill="var(--blue)"/>
    <path d="M0 354 C90 389 190 334 290 366 L290 372 C190 340 90 395 0 360Z" fill="var(--green)"/>
  </svg>
  <div class="brand"><span class="brand-mark"></span><span class="brand-name">ORB</span><span class="brand-tag">Outreach Regional<br>Bureau of Climate<br>Partners</span></div>
  <div class="contact">T 555 014 2200<br>F 555 014 2201<br>12 Ridge Lane<br>Aspen Falls CO<br>dpalvane@qzr.example</div>
  <div class="ghost-name">ORB</div>
</div>
<p class="label" style="left:574px;top:432px">Letterhead Option 2</p>

<div class="sheet envelope-back">
  <svg class="waves" viewBox="0 0 330 216" preserveAspectRatio="none" aria-hidden="true">
    <path d="M0 0 L330 0 L330 30 C250 50 210 95 165 95 C120 95 80 50 0 30Z" fill="var(--green)"/>
    <path d="M0 30 C80 50 120 95 165 95 C210 95 250 50 330 30" fill="none" stroke="#5aa024" stroke-width="1"/>
  </svg>
</div>

<div class="sheet envelope-plain">
  <svg class="waves" viewBox="0 0 330 118" preserveAspectRatio="none" aria-hidden="true">
    <path d="M0 6 C90 20 120 58 165 58 C210 58 240 20 330 6" fill="none" stroke="#cfcfcf" stroke-width="1"/>
  </svg>
</div>

<div class="sheet envelope-front">
  <svg class="waves" viewBox="0 0 283 112" preserveAspectRatio="none" aria-hidden="true">
    <path d="M0 92 C80 80 170 106 283 84 L283 112 L0 112Z" fill="var(--blue)"/>
    <path d="M0 88 C80 76 170 102 283 80 L283 84 C170 106 80 80 0 92Z" fill="var(--green)"/>
  </svg>
  <div class="brand"><span class="brand-mark"></span><span class="brand-name">ORB</span><span class="brand-tag">Outreach Regional<br>Bureau of Climate<br>Partners</span></div>
  <p class="return">12 Ridge Lane, Aspen Falls CO &middot; www.orbworthkeeping.example</p>
</div>
<p class="label" style="left:900px;top:413px">Envelope Option 2</p>

</body>
</html>
```